property investment and development company needs a website

we need a website that looks professional and portrays trust for people looking to us to buy their house or investors looking to invest or joint venture with us.
We are based in the west midlands in the UK.
we deal mainly with residential housing, house to flats conversions, HMO's (houses in multiple ocupancy).
we require the website as a first point of contact with potential sellers, renters and investors so links or contact details that are easy to access or see would be good.
I have had logos designed by a plan hollow member and these can be used as guidance for the colour and style of the site.
Target Market(s)
joint venture investment partners, people looking to sell their house, people looking to rent from us.
Coding
Coded - Design and coding required
Number of Pages Required
3 page
Requirements
Must have
- project a professional appearance
- visable contact details

```html
<!DOCTYPE html>
<html lang="en">
<head>
<meta charset="utf-8">
<title>Ashford Homes</title>
<link rel="stylesheet" href="https://fonts.googleapis.com/css2?family=Cinzel:wght@400;600&family=Lato:wght@400;700&display=swap">
<style>
:root{
  --charcoal:#3b3b3c;
  --charcoal-deep:#2f2f30;
  --gold:#c6a66b;
  --gold-dark:#b8955a;
  --ink:#222222;
  --body:#3d3d3d;
  --white:#ffffff;
  --line:#cfcfcf;
  --map:#d9d9d7;
}
*{box-sizing:border-box;margin:0;padding:0}
html,body{width:1200px;height:2675px;overflow:hidden}
body{font-family:"Lato",sans-serif;color:var(--body);background:var(--white);position:relative}
.serif{font-family:"Cinzel",serif}
section,header,footer{position:absolute;left:0;width:1200px}

/* header */
.site-header{top:0;height:107px;background:var(--charcoal)}
.brand{position:absolute;left:120px;top:24px;display:flex;align-items:center;gap:14px}
.brand-dot{width:50px;height:50px;border-radius:50%;background:var(--gold)}
.brand-name{font-family:"Cinzel",serif;color:var(--white);font-size:30px;line-height:30px;letter-spacing:1px}
.main-nav{position:absolute;left:490px;top:47px;display:flex;align-items:center}
.main-nav a{font-family:"Cinzel",serif;color:var(--white);text-decoration:none;font-size:15px;letter-spacing:1px}
.main-nav .sep{width:1px;height:14px;background:#666;margin:0 30px}
.main-nav a.active{color:var(--gold);border-bottom:1px solid var(--gold);padding-bottom:3px}

/* hero */
.hero{top:107px;height:623px}
.hero-photo{position:absolute;inset:0;background:linear-gradient(110deg,#2a2e35 0%,#5f6670 20%,#a8c4d6 45%,#cfdfe8 65%,#7fa2bc 100%)}
.hero-chart{position:absolute;left:300px;top:20px}
.hero-caption{position:absolute;left:0;bottom:0;width:100%;height:66px;background:rgba(40,40,40,.55);display:flex;align-items:center;justify-content:center}
.hero-caption h1{font-family:"Cinzel",serif;font-weight:400;color:var(--white);font-size:28px;letter-spacing:1.5px}
.hero-arrow{position:absolute;top:22px}

/* about */
.about{top:730px;height:527px}
.about-mark{position:absolute;left:125px;top:110px;width:300px;height:300px;display:flex;flex-direction:column;align-items:center;justify-content:center;gap:22px}
.about-mark .ring{width:150px;height:150px;border-radius:50%;background:var(--gold)}
.about-mark .word{font-family:"Cinzel",serif;color:var(--gold);font-size:32px;letter-spacing:2px}
.about-rule{position:absolute;left:460px;top:120px;width:1px;height:300px;background:var(--line)}
.about-text{position:absolute;left:498px;top:145px;width:585px}
.about-text h2{font-family:"Cinzel",serif;font-weight:400;font-size:30px;color:var(--ink);letter-spacing:1px;margin-bottom:28px}
.about-text p{font-size:12.5px;line-height:17px;margin-bottom:12px;color:var(--body)}
.btn-outline{display:inline-block;margin-top:14px;width:158px;height:38px;border:1px solid var(--gold);color:var(--gold);font-size:13px;line-height:36px;text-align:center}

/* invest / sell */
.split{top:1257px;height:540px}
.panel{position:absolute;top:0;width:600px;height:540px;color:var(--white);text-align:center}
.panel-invest{left:0;background:linear-gradient(160deg,#d7b87c 0%,#c9a565 55%,#b99152 100%)}
.panel-sell{left:600px;background:linear-gradient(165deg,#13284a 0%,#3a4a5c 45%,#6b6650 75%,#3c4a2c 100%)}
.panel-sell .shade{position:absolute;inset:0;background:rgba(20,25,35,.45)}
.panel-body{position:absolute;left:130px;top:85px;width:340px}
.panel h2{font-family:"Cinzel",serif;font-weight:400;font-size:29px;letter-spacing:1px;margin-bottom:10px}
.panel-invest h2{color:var(--ink)}
.panel-sell h2{color:var(--gold)}
.panel .bar{width:60px;height:2px;background:var(--white);margin:0 auto 28px}
.panel-invest .panel-body{left:130px;width:470px;left:65px}
.panel p{font-size:12px;line-height:18px;margin-bottom:20px}
.panel-invest p{color:#2d2a24}
.panel-sell .panel-body{left:45px;width:510px}
.panel .tel{font-weight:700;font-size:15px}
.btn-dark,.btn-gold{display:inline-block;height:38px;line-height:38px;font-size:13px;font-weight:700;color:var(--white);padding:0 20px;margin-top:8px}
.btn-dark{background:#2f2f30}
.btn-gold{background:var(--gold)}

/* subscribe */
.subscribe{top:1797px;height:251px}
.subscribe h2{position:absolute;left:120px;top:97px;font-family:"Cinzel",serif;font-weight:400;color:var(--gold);font-size:26px;letter-spacing:1px}
.subscribe h3{position:absolute;left:120px;top:131px;font-size:16px;font-weight:700;color:var(--ink)}
.sub-field{position:absolute;left:550px;top:100px;width:530px;height:54px;border:1px solid var(--line);border-radius:27px;font-size:11px;color:#9a9a9a;line-height:52px;padding-left:14px}
.sub-btn{position:absolute;left:902px;top:100px;width:178px;height:54px;border-radius:27px;background:var(--gold);color:var(--white);font-weight:700;font-size:16px;text-align:center;line-height:54px}

/* contact */
.contact{top:2048px;height:482px}
.map{position:absolute;inset:0;background:linear-gradient(120deg,#d2d3cf 0%,#e0e0dc 50%,#cfd1cb 100%)}
.details{position:absolute;left:190px;top:222px;width:422px;height:260px;background:rgba(40,40,40,.82);padding:22px 22px;color:var(--white)}
.details h3{font-family:"Cinzel",serif;font-weight:400;color:var(--gold);font-size:17px;letter-spacing:1px;margin-bottom:14px}
.details li{list-style:none;display:flex;align-items:center;gap:12px;font-size:13px;height:24px}
.details svg{flex:none}
.form-card{position:absolute;left:595px;top:89px;width:485px;height:323px;background:var(--white);padding:22px 34px}
.form-card h2{font-family:"Cinzel",serif;font-weight:400;color:var(--gold);font-size:24px;letter-spacing:1px;margin-bottom:12px}
.form-grid{display:grid;grid-template-columns:203px 203px;gap:9px 12px}
.form-grid div{height:38px;border:1px solid var(--line);font-size:11px;color:#8a8a8a;padding:8px 8px}
.form-grid .message{grid-column:1 / 3;height:88px}
.send{display:inline-block;margin-top:11px;width:172px;height:36px;border-radius:18px;background:var(--gold);color:var(--white);font-weight:700;font-size:15px;text-align:center;line-height:36px}

/* footer */
.site-footer{top:2530px;height:145px;background:var(--charcoal)}
.foot-nav{position:absolute;left:118px;top:48px;display:flex;align-items:center}
.foot-nav a{color:var(--white);text-decoration:none;font-size:11.5px;letter-spacing:.5px}
.foot-nav .sep{width:1px;height:12px;background:#777;margin:0 40px}
.copyright{position:absolute;left:118px;top:84px;color:var(--white);font-size:11px}
.follow{position:absolute;left:923px;top:40px;color:var(--gold);font-size:19px;font-weight:700}
.social{position:absolute;left:922px;top:73px;display:flex;gap:13px}
.social span{width:30px;height:30px;border-radius:50%;background:#e6e6e6}
.social span:first-child{background:var(--gold)}
</style>
</head>
<body>

<header class="site-header">
  <div class="brand"><span class="brand-dot"></span><span class="brand-name">ASHFORD<br>HOMES</span></div>
  <nav class="main-nav">
    <a class="active">HOME</a><span class="sep"></span>
    <a>ABOUT US</a><span class="sep"></span>
    <a>INVEST</a><span class="sep"></span>
    <a>SELL</a><span class="sep"></span>
    <a>CONTACT US</a>
  </nav>
</header>

<section class="hero">
  <div class="hero-photo" role="img" aria-label="Businessman holding a tablet beside a city skyline with a rising growth arrow"></div>
  <div class="hero-caption">
    <svg class="hero-arrow" style="left:82px" width="14" height="22" viewBox="0 0 14 22"><path d="M12 1 2 11l10 10" fill="none" stroke="#fff" stroke-width="2"/></svg>
    <h1>WEARE A PROPERTY DEVELOPMENT AND INVESTMENT COMPANY</h1>
    <svg class="hero-arrow" style="right:82px" width="14" height="22" viewBox="0 0 14 22"><path d="M2 1l10 10L2 21" fill="none" stroke="#fff" stroke-width="2"/></svg>
  </div>
</section>

<section class="about">
  <div class="about-mark"><span class="ring"></span><span class="word">ASHFORD HOMES</span></div>
  <div class="about-rule"></div>
  <div class="about-text">
    <h2>ABOUT ASHFORD HOMES</h2>
    <p>Weare a property development and investment company that have our own portfolio and we are active investorswho pride ourselves in expanding our business organically.</p>
    <p>We ensure that whatever your property needs are we deliver bespoke services for our clients. For investors, sellers, landlords and tenants we bring knowledge to your next property decision, allowing you to make an informed decision.</p>
    <span class="btn-outline">READ MORE ››</span>
  </div>
</section>

<section class="split">
  <div class="panel panel-invest" role="img" aria-label="Hands cupped around a small model house in warm gold light">
    <div class="panel-body">
      <h2>INVEST</h2>
      <div class="bar"></div>
      <p>We have our own portfolio and we are active investors, so our finger is on the pulse and we are currently looking for residential development investments &amp; commercial to residential conversions in cities or regional centres showing strong growth.</p>
      <p>Our experience in the industry enables us to make extremely quick andwell-informed decisions. We follow the opportunities that are presented to us as well as sourcing opportunities ourselves.We are happy to work in partnership and within joint ventures and have a proven track record of establishing excellent relationships in these areas.</p>
      <span class="btn-dark">READ MORE ››</span>
    </div>
  </div>
  <div class="panel panel-sell" role="img" aria-label="Hand holding house keys in front of a family home at dusk">
    <div class="shade"></div>
    <div class="panel-body">
      <h2>SELL</h2>
      <div class="bar"></div>
      <p>We undertake the necessary market research to evaluate an option that works for all parties involved. We will help guide you to make an informed decision on how to gain the maximum realistic value.</p>
      <p>For those looking to achieve a fast and professional sale to experienced investors, we provide an approach that has been proven to work for many others.</p>
      <p>If you would like to discuss a property you are looking to sell,<br>then please contact us on <span class="tel">01632 960448</span></p>
      <span class="btn-gold">CALL US TODAY ››</span>
    </div>
  </div>
</section>

<section class="subscribe">
  <h2>ARE YOU INVEST OR SELLING?</h2>
  <h3>SEARCH YOUR DREAM HOME</h3>
  <div class="sub-field">your email adddress</div>
  <div class="sub-btn">SUBSCRIBE NOW</div>
</section>

<section class="contact">
  <div class="map" role="img" aria-label="Street map of the office surroundings with a location pin"></div>
  <div class="details">
    <h3>COMPANY DETAILS</h3>
    <ul>
      <li><svg width="14" height="14" viewBox="0 0 24 24"><path d="M6.6 10.8a15 15 0 0 0 6.6 6.6l2.2-2.2a1 1 0 0 1 1-.2 11 11 0 0 0 3.6.6 1 1 0 0 1 1 1V20a1 1 0 0 1-1 1A17 17 0 0 1 3 4a1 1 0 0 1 1-1h3.5a1 1 0 0 1 1 1 11 11 0 0 0 .6 3.6 1 1 0 0 1-.3 1z" fill="#c6a66b"/></svg>01632 960448</li>
      <li><svg width="14" height="14" viewBox="0 0 24 24"><path d="M6.6 10.8a15 15 0 0 0 6.6 6.6l2.2-2.2a1 1 0 0 1 1-.2 11 11 0 0 0 3.6.6 1 1 0 0 1 1 1V20a1 1 0 0 1-1 1A17 17 0 0 1 3 4a1 1 0 0 1 1-1h3.5a1 1 0 0 1 1 1 11 11 0 0 0 .6 3.6 1 1 0 0 1-.3 1z" fill="#c6a66b"/></svg>07700 900109</li>
      <li><svg width="14" height="14" viewBox="0 0 24 24"><rect x="2" y="5" width="20" height="14" fill="#c6a66b"/><path d="M2 5l10 8 10-8" fill="none" stroke="#333" stroke-width="1.6"/></svg>info@ashfordhomes.co.uk</li>
      <li><svg width="14" height="14" viewBox="0 0 24 24"><path d="M12 2a7 7 0 0 0-7 7c0 5 7 13 7 13s7-8 7-13a7 7 0 0 0-7-7zm0 9.5A2.5 2.5 0 1 1 12 6.5a2.5 2.5 0 0 1 0 5z" fill="#c6a66b"/></svg>12 Fenwick Road, Elmbury, Westshire, WR0 0AA</li>
    </ul>
  </div>
  <div class="form-card">
    <h2>CONTACT US</h2>
    <div class="form-grid">
      <div>Your Name</div><div>Your Email</div>
      <div>Your Phone</div><div>Subject</div>
      <div class="message">Your Message</div>
    </div>
    <span class="send">SEND MESSAGE ››</span>
  </div>
</section>

<footer class="site-footer">
  <nav class="foot-nav">
    <a>HOME</a><span class="sep"></span>
    <a>ABOUT US</a><span class="sep"></span>
    <a>INVEST</a><span class="sep"></span>
    <a>SELL</a><span class="sep"></span>
    <a>CONTACT US</a>
  </nav>
  <p class="copyright">Copyright © 2019 ASHFORD HOMES. All Right Reserved</p>
  <p class="follow">Follow Us On :</p>
  <div class="social" aria-label="Social network links"><span></span><span></span><span></span><span></span></div>
</footer>

</body>
</html>
```